harborKettrix.com Blog/website

This is new site, we do not have any current content
Would like a website for harbor kettrix. The site will cover what to expect getting started, what to wear. How to pick out a kettrix Gym (called a box).
We will be posting articles on exercises and how to properly perform and occasional product review.
We would like a section on recipes and what to eat and not to eat
We are attempting to remove the barrier of entry to get new people transform their lives/body and try kettrix.
Will also like to post daily Work outs which are called WODs (workout of the day) and exercises.
The sections of the site I envision are
• the front landing page
• Contact Page
• Blog Page
• About Page
• Recipe Page
• Exercise Page
• FAQ and frequently used Terms

Target Market(s)

Fitness market, people interested or just starting kettrix

Industry/Entity Type

Fitness

Logo Text

harbor Kettrix - your kettrix start page - or something like that

Coding

Coded - Design and coding required

Number of Pages Required

5+ page

Font styles to use
Sans Serif

Requirements
Must have
• Frontpage, Contact Page, Blog Page, about page and FAQ and Terms Page
• This will be on a wordpress site
Nice to have
• would like to have more of a female slant and feel. photos of workouts

```html
<!DOCTYPE html>
<html lang="en">
<head>
<meta charset="utf-8">
<title>Harbor Kettrix – Fitness Gym</title>
<link rel="stylesheet" href="https://fonts.googleapis.com/css2?family=Michroma&family=Open+Sans:wght@400;600;700&family=Syncopate:wght@700&display=swap">
<style>
  :root{
    --red:#d3202b;
    --ink:#1d1d1d;
    --black:#050505;
    --white:#ffffff;
    --muted:#9a9a9a;
    --soft:#f2f2f2;
    --line:#e2e2e2;
    --head:"Michroma", sans-serif;
    --body:"Open Sans", sans-serif;
  }
  *{box-sizing:border-box;margin:0;padding:0}
  html,body{width:1200px;height:4054px;overflow:hidden}
  body{font-family:var(--body);color:var(--ink);background:var(--white);position:relative}
  section,header,footer{position:absolute;left:0;width:1200px}
  .abs{position:absolute}
  .red{color:var(--red)}
  .section-title{font-family:var(--head);font-size:30px;letter-spacing:1px;text-align:center;width:100%;position:absolute;left:0}
  .title-mark{position:absolute;left:450px;width:300px;height:20px}
  .title-mark::before{content:"";position:absolute;left:0;right:0;top:9px;height:1px;background:currentColor;opacity:.35}
  .title-mark::after{content:"";position:absolute;left:140px;top:0;width:20px;height:20px;background:var(--red)}
  .photo{position:absolute}

  /* hero */
  .hero{top:0;height:676px;background:linear-gradient(100deg,#2b2b2b 0%,#474747 30%,#1e1e1e 60%,#0f0f0f 100%)}
  .brand{position:absolute;left:76px;top:40px;display:flex;align-items:center;gap:12px}
  .brand-square{width:34px;height:34px;background:var(--red)}
  .brand-name{font-family:var(--body);font-weight:700;font-size:22px;letter-spacing:2px;color:var(--white)}
  .nav{position:absolute;left:460px;top:54px;display:flex;align-items:center;font-size:14px;color:var(--white)}
  .nav a{color:inherit;text-decoration:none;padding:0 14px;line-height:54px}
  .nav a.active{border:3px solid var(--white);padding:0 24px;margin-right:10px}
  .hero-title{position:absolute;right:81px;top:310px;text-align:right;font-family:"Syncopate",sans-serif;font-weight:700;font-size:40px;line-height:48px;color:var(--white);letter-spacing:1px}
  .hero-sub{position:absolute;right:81px;top:418px;text-align:right;font-size:16px;line-height:26px;color:var(--white);text-transform:uppercase}
  .dots{position:absolute;right:86px;top:502px;display:flex;gap:8px}
  .dots span{width:11px;height:11px;background:var(--white)}
  .dots span.on{background:transparent;border:2px solid var(--white)}

  /* welcome */
  .welcome{top:676px;height:346px;background:var(--white);color:#222}
  .welcome .title-mark{color:#333}
  .welcome p{position:absolute;left:220px;width:760px;top:180px;font-size:13px;line-height:24px;color:var(--muted);text-align:center}

  /* exercises */
  .exercises{top:1022px;height:730px;background:linear-gradient(180deg,#181818 0%,#2e2e2e 45%,#141414 100%);color:var(--white)}
  .exercises .title-mark{color:var(--white)}
  .ex-text{position:absolute;width:300px}
  .ex-text h4{font-size:14px;font-weight:700;letter-spacing:.3px}
  .ex-text p{font-size:13px;line-height:24px;margin-top:6px;color:#e8e8e8}
  .ex-icon{position:absolute;width:97px;height:97px;border:3px solid var(--white);display:flex;align-items:center;justify-content:center}
  .ex-icon.on{border-color:var(--red)}
  .pill{position:absolute;border-radius:40px;display:flex;align-items:center;justify-content:center;font-weight:600;letter-spacing:1px;font-size:15px}
  .btn-view{left:497px;top:603px;width:206px;height:66px;background:var(--white);color:var(--ink)}

  /* recipes */
  .recipes{top:1752px;height:481px;background:var(--white)}
  .recipes-panel{position:absolute;left:0;top:0;width:624px;height:481px;background:var(--soft)}
  .recipes-panel .section-title{width:624px;top:60px}
  .recipes-panel .sub{position:absolute;left:0;width:624px;top:108px;text-align:center;font-size:13px;color:var(--muted)}
  .btn-more{left:211px;top:362px;width:205px;height:65px;border:2px solid var(--red);color:var(--red);background:transparent}

  /* newsletter */
  .newsletter{top:2233px;height:157px;background:var(--red)}
  .news-field{position:absolute;left:238px;top:51px;width:505px;height:57px;border:2px solid var(--white);border-radius:30px;color:var(--white);font-size:14px;padding-left:28px;line-height:53px}
  .news-btn{left:757px;top:51px;width:203px;height:57px;background:var(--white);color:var(--red);font-size:15px}

  /* content */
  .content{top:2390px;height:1016px;background:var(--white)}
  .h-left{position:absolute;font-family:var(--head);font-size:30px;letter-spacing:1px;line-height:40px}
  .card h5{position:absolute;font-size:15px;font-weight:700}
  .card p{position:absolute;font-size:13px;line-height:25px;color:#666}
  .divider{position:absolute;height:1px;background:var(--line)}
  .faq{position:absolute;left:781px;top:164px;width:345px;list-style:none}
  .faq li{font-size:12px;line-height:20px;color:#8a8a8a;padding:6px 0 6px 22px;position:relative;border-bottom:1px solid #f0f0f0}
  .faq li::before{content:"";position:absolute;left:4px;top:14px;width:6px;height:6px;border-radius:50%;background:#b5b5b5}
  .faq li.on{color:var(--red)}
  .faq li.on::before{background:var(--red)}
  .posted{position:absolute;font-size:13px;color:#555}
  .posted span{color:#bbb}

  /* connected */
  .connected{top:3406px;height:270px;background:var(--soft)}
  .connected p{position:absolute;left:300px;width:600px;top:110px;text-align:center;font-size:13px;line-height:24px;color:var(--muted)}
  .socials{position:absolute;left:524px;top:188px;display:flex;gap:14px}
  .socials span{width:27px;height:27px;border:1px solid #c9c9c9;background:var(--white)}
  .socials span.on{border-color:var(--red)}

  /* footer */
  .footer{top:3676px;height:378px;background:var(--black);color:var(--white)}
  .footer .brand{left:0;width:1200px;top:85px;justify-content:center}
  .footer .brand-name{font-size:30px}
  .footer .brand-square{width:44px;height:44px}
  .foot-nav{position:absolute;left:0;width:1200px;top:225px;display:flex;justify-content:center;font-size:14px;color:#999}
  .foot-nav a{color:inherit;text-decoration:none;padding:0 24px;border-left:1px solid #444}
  .foot-nav a:first-child{border-left:0;color:var(--white)}
  .foot-line{position:absolute;left:211px;width:778px;top:262px;height:1px;background:#333}
  .copy{position:absolute;left:0;width:1200px;top:293px;text-align:center;font-size:12px;color:#bbb}
</style>
</head>
<body>

<header class="hero">
  <div class="photo" role="img" aria-label="Athlete training with a dumbbell in a dark gym" style="left:0;top:0;width:640px;height:676px;background:radial-gradient(ellipse at 40% 55%,#6a6a6a 0%,#3a3a3a 45%,rgba(30,30,30,0) 75%)"></div>
  <div class="brand"><span class="brand-square"></span><span class="brand-name">HARBOR KETTRIX</span></div>
  <nav class="nav">
    <a class="active" href="#">Home</a><a href="#">About Us</a><a href="#">Exercise</a><a href="#">Recipes</a><a href="#">FAQ</a><a href="#">Blog</a><a href="#">Contact Us</a>
  </nav>
  <h1 class="hero-title">KETTRIX<br>FITNESS GYM</h1>
  <p class="hero-sub">Push yourself to yur limits achive<br>your fitness goals</p>
  <div class="dots"><span></span><span class="on"></span><span></span></div>
</header>

<section class="welcome">
  <h2 class="section-title" style="top:74px">WELCOME TO <span class="red">KETTRIX</span></h2>
  <div class="title-mark" style="top:120px"></div>
  <p>Lorem ipsum dolor sit amet, consectetur adipiscing elit, sed do eiusmod tempor incididunt ut labore et dolore magna aliqua. Ut enim ad minim veniam, quis nostrud exercitation ullamco laboris nisi ut aliquip ex ea commodo consequat. Duis aute irure dolor in reprehenderit in voluptate velit esse cillum dolore eu fugiat nulla pariatur.</p>
</section>

<section class="exercises">
  <h2 class="section-title" style="top:72px">SEE OUR EXERCIES</h2>
  <div class="title-mark" style="top:122px"></div>

  <div class="ex-text" style="left:162px;top:210px"><h4 class="red">LOREM IPSUM DOLOR SIT AMET</h4><p>Consectetur adipiscing elit, sed do eiusmod tempor incididunt ut labore et dolore magna.</p></div>
  <div class="ex-text" style="left:162px;top:334px"><h4>LOREM IPSUM DOLOR SIT AMET</h4><p>Consectetur adipiscing elit, sed do eiusmod tempor incididunt ut labore et dolore magna.</p></div>
  <div class="ex-text" style="left:162px;top:458px"><h4>LOREM IPSUM DOLOR SIT AMET</h4><p>Consectetur adipiscing elit, sed do eiusmod tempor incididunt ut labore et dolore magna.</p></div>
  <div class="ex-text" style="left:741px;top:210px"><h4>LOREM IPSUM DOLOR SIT AMET</h4><p>Consectetur adipiscing elit, sed do eiusmod tempor incididunt ut labore et dolore magna.</p></div>
  <div class="ex-text" style="left:741px;top:334px"><h4>LOREM IPSUM DOLOR SIT AMET</h4><p>Consectetur adipiscing elit, sed do eiusmod tempor incididunt ut labore et dolore magna.</p></div>
  <div class="ex-text" style="left:741px;top:458px"><h4>LOREM IPSUM DOLOR SIT AMET</h4><p>Consectetur adipiscing elit, sed do eiusmod tempor incididunt ut labore et dolore magna.</p></div>

  <div class="ex-icon on" style="left:497px;top:200px"><svg width="50" height="24" viewBox="0 0 50 24"><rect x="0" y="4" width="8" height="16" fill="#fff"/><rect x="42" y="4" width="8" height="16" fill="#fff"/><rect x="8" y="10" width="34" height="4" fill="#fff"/></svg></div>
  <div class="ex-icon" style="left:611px;top:200px"><svg width="36" height="40" viewBox="0 0 36 40"><path d="M10 10h16" stroke="#fff" stroke-width="4" fill="none"/><circle cx="18" cy="26" r="13" fill="#fff"/></svg></div>
  <div class="ex-icon" style="left:497px;top:324px"><svg width="50" height="24" viewBox="0 0 50 24"><rect x="0" y="4" width="8" height="16" fill="#fff"/><rect x="42" y="4" width="8" height="16" fill="#fff"/><rect x="8" y="10" width="34" height="4" fill="#fff"/></svg></div>
  <div class="ex-icon" style="left:611px;top:324px"><svg width="36" height="40" viewBox="0 0 36 40"><path d="M10 10h16" stroke="#fff" stroke-width="4" fill="none"/><circle cx="18" cy="26" r="13" fill="#fff"/></svg></div>
  <div class="ex-icon" style="left:497px;top:448px"><svg width="40" height="40" viewBox="0 0 40 40"><circle cx="20" cy="20" r="16" fill="none" stroke="#fff" stroke-width="4"/><path d="M20 10v10l7 5" stroke="#fff" stroke-width="4" fill="none"/></svg></div>
  <div class="ex-icon" style="left:611px;top:448px"><svg width="40" height="30" viewBox="0 0 40 30"><path d="M4 15h26M22 6l10 9-10 9" stroke="#fff" stroke-width="4" fill="none"/></svg></div>

  <a class="pill btn-view">VIEW ALL</a>
</section>

<section class="recipes">
  <div class="recipes-panel">
    <h2 class="section-title">GET OUR <span class="red">RECIPES</span></h2>
    <p class="sub">What You have to Eat during Exercise, And What Do not Eat</p>
    <div class="photo" role="img" aria-label="Fresh green salad" style="left:76px;top:175px;width:143px;height:143px;background:linear-gradient(135deg,#7fae4a,#c8d89a 55%,#f2f2ee)"></div>
    <div class="photo" role="img" aria-label="Mixed salad with tomatoes" style="left:246px;top:175px;width:141px;height:143px;background:linear-gradient(135deg,#b84a36,#8aa456 50%,#e9e4d6)"></div>
    <div class="photo" role="img" aria-label="Omelette on a plate" style="left:414px;top:175px;width:143px;height:143px;background:linear-gradient(135deg,#d9c86a,#f0e7b8 50%,#f7f6f0)"></div>
    <a class="pill btn-more">GET MORE</a>
  </div>
  <div class="photo" role="img" aria-label="Woman choosing between junk food and fruit and vegetables" style="left:676px;top:86px;width:497px;height:352px;background:radial-gradient(ellipse at 50% 55%,#f1ece6 0%,#e9c7a0 30%,rgba(255,255,255,0) 72%)"></div>
</section>

<section class="newsletter">
  <div class="news-field">NEWSLETTER</div>
  <a class="pill news-btn">SUBSCRIBE</a>
</section>

<section class="content">
  <h2 class="h-left" style="left:81px;top:55px">WORKOUT <span class="red">OF THE DAY</span></h2>
  <div class="photo" role="img" aria-label="Woman doing a plank with dumbbells" style="left:81px;top:135px;width:206px;height:113px;background:linear-gradient(135deg,#5b5650,#a9a39c)"></div>
  <div class="photo" role="img" aria-label="Woman doing a plank on a mat" style="left:303px;top:135px;width:205px;height:113px;background:linear-gradient(135deg,#c9d2da,#8ea0b0)"></div>
  <div class="photo" role="img" aria-label="Woman stretching on the floor" style="left:524px;top:135px;width:209px;height:113px;background:linear-gradient(135deg,#6b6b6b,#cfcfcf)"></div>
  <div class="card">
    <h5 style="left:81px;top:270px">LOREM IPSUM</h5><p style="left:81px;top:296px;width:206px">Consectetur adipiscing eli sed do eiusmod...<span class="red">»</span></p>
    <h5 style="left:303px;top:270px">LOREM IPSUM</h5><p style="left:303px;top:296px;width:205px">Consectetur adipiscing eli sed do eiusmod...<span class="red">»</span></p>
    <h5 style="left:524px;top:270px">LOREM IPSUM</h5><p style="left:524px;top:296px;width:209px">Consectetur adipiscing eli sed do eiusmod...<span class="red">»</span></p>
  </div>
  <div class="divider" style="left:81px;top:394px;width:652px"></div>

  <h2 class="h-left" style="left:81px;top:442px">SEE OUR <span class="red">LATEST BLOG</span></h2>
  <div class="photo" role="img" aria-label="Woman stretching on an exercise ball" style="left:81px;top:521px;width:311px;height:176px;background:linear-gradient(135deg,#5d7fa0,#c7d3dd 60%,#eef1f4)"></div>
  <div class="photo" role="img" aria-label="Woman lifting a dumbbell" style="left:422px;top:521px;width:311px;height:176px;background:linear-gradient(135deg,#2f4960,#c9b29b 55%,#e6e3df)"></div>
  <div class="card">
    <h5 style="left:81px;top:730px">LOREM IPSUM</h5><p style="left:81px;top:757px;width:311px">Consectetur adipiscing elit, sed do eiusmod tempor incididunt ut labore et.</p>
    <h5 style="left:422px;top:730px">LOREM IPSUM</h5><p style="left:422px;top:757px;width:311px">Consectetur adipiscing elit, sed do eiusmod tempor incididunt ut labore et.</p>
  </div>
  <p class="posted" style="left:81px;top:852px">Posted on <span>23rd march,2016</span></p>
  <p class="posted" style="left:422px;top:852px">Posted on <span>23rd march,2016</span></p>

  <h2 class="h-left" style="left:781px;top:55px">FREQUENTLY<br>ASK <span class="red">QUESTIONS</span></h2>
  <ul class="faq">
    <li class="on">Lorem ipsum dolor sit amet, consectetur ?</li>
    <li>adipiscing elit, sed do eiusmod tempor incididunt ut labore et dolore ?</li>
    <li>Lorem ipsum dolor sit amet, consectetur ?</li>
    <li>Lorem ipsum dolor sit amet, consectetur ?</li>
    <li>adipiscing elit, sed do eiusmod tempor incididunt ut labore et dolore ?</li>
    <li>Lorem ipsum dolor sit amet, consectetur ?</li>
    <li>adipiscing elit, sed do eiusmod tempor incididunt ut labore et dolore ?</li>
    <li>Lorem ipsum dolor sit amet, consectetur ?</li>
    <li>Lorem ipsum dolor sit amet, consectetur ?</li>
  </ul>
  <div class="divider" style="left:781px;top:594px;width:345px"></div>

  <h2 class="h-left" style="left:781px;top:638px">OUR <span class="red">GALLERY</span></h2>
  <div class="photo" role="img" aria-label="Gym training photo" style="left:765px;top:724px;width:108px;height:108px;background:linear-gradient(135deg,#2a2a2a,#8c8c8c)"></div>
  <div class="photo" role="img" aria-label="Gym training photo" style="left:889px;top:724px;width:108px;height:108px;background:linear-gradient(135deg,#6d7a86,#d6dbe0)"></div>
  <div class="photo" role="img" aria-label="Gym training photo" style="left:1014px;top:724px;width:108px;height:108px;background:linear-gradient(135deg,#3a3a3a,#a8a8a8)"></div>
  <div class="photo" role="img" aria-label="Gym training photo" style="left:765px;top:848px;width:108px;height:114px;background:linear-gradient(135deg,#1f1f1f,#7a7a7a)"></div>
  <div class="photo" role="img" aria-label="Gym training photo" style="left:889px;top:848px;width:108px;height:114px;background:linear-gradient(135deg,#b7b7b7,#4d4d4d)"></div>
  <div class="photo" role="img" aria-label="Gym training photo" style="left:1014px;top:848px;width:108px;height:114px;background:linear-gradient(135deg,#161616,#6c5a4a)"></div>
</section>

<section class="connected">
  <h2 class="section-title" style="top:56px">STAY <span class="red">CONNECTED</span></h2>
  <p>Lorem ipsum dolor sit amet, consectetur adipiscing elit, sed do eiusmod tempor incididunt ut labore et dolore magna aliqua</p>
  <div class="socials"><span></span><span class="on"></span><span></span><span></span></div>
</section>

<footer class="footer">
  <div class="brand"><span class="brand-square"></span><span class="brand-name">HARBOR KETTRIX</span></div>
  <nav class="foot-nav"><a href="#">Home</a><a href="#">About Us</a><a href="#">Exercise</a><a href="#">Recipes</a><a href="#">FAQ</a><a href="#">Blog</a><a href="#">Contact Us</a></nav>
  <div class="foot-line"></div>
  <p class="copy">© <span class="red">KETTRIX</span> - 2016. All rights Reserved.</p>
</footer>

</body>
</html>
```